Lakemont Harmony Medical Tri-Fold Flyer

a marketing 3- fold flyer for primary business awareness. this should offer all aspects of our medical practice. I have provided several pictures as well as all pertinent information needed to make a successful flyer. This needs to be eye catching and attractive. each page should feature something of its own.
my thoughts:
page 1- photo of office our mission statement and maybe our phone number and address
page 2- our LHM A-team flyer
page 3- our paragraph on our practice as well as some of our services. say something like we offer a wide scope of services including health coaching, weight loss. A "patient services coordinator" will help you pick out what services we can do for you. a pic
page 4- doctors bio and pics and logos
page 5-
page 6- our map our address and phone numbers. the sentence on making an appointment. our web page and facebook as well as our logos

Target Market(s)

we are a medical practice, so we are seeking new patients

Industry/Entity Type

Health Care

Font styles to use
Serif

Colors
34a6d7
33b8a4
abd036
fbee3e

Requirements
Must have
• I have enclosed a tri-fold info attachment as well as other pieces. Use what you feel will make our flyer attractive. Not too busy. Please try to get most info in
• All work purchased should be delivered with the PDF form for future changes by owner of medical office.
Nice to have
• All Info provided

```html
<!DOCTYPE html>
<html lang="en">
<head>
<meta charset="utf-8">
<title>Lakemont Harmony Medical – Flyer Cover Panel</title>
<link rel="stylesheet" href="https://fonts.googleapis.com/css2?family=Roboto:wght@300;400;700&display=swap">
<style>
  :root {
    --backdrop: #b9b8bd;
    --sky-deep: #2a63b8;
    --sky-mid: #4f92dc;
    --sky-pale: #9cc6ee;
    --band-green: #abd036;
    --headline-blue: #7fb6e6;
    --headline-green: #abd036;
    --brand-blue: #34a6d7;
    --paper: #ffffff;
    --ink-white: #ffffff;
  }
  * { margin: 0; padding: 0; box-sizing: border-box; }
  html, body { width: 1200px; height: 900px; overflow: hidden; }
  body {
    background: var(--backdrop);
    font-family: "Roboto", "Helvetica Neue", Arial, sans-serif;
    display: flex;
    align-items: center;
    justify-content: center;
  }
  .flyer-panel {
    position: relative;
    width: 354px;
    height: 820px;
    background: var(--paper);
    overflow: hidden;
  }
  .panel-shapes { position: absolute; inset: 0; }
  .headline {
    position: absolute;
    top: 38px;
    left: 38px;
    font-weight: 300;
    line-height: 1.05;
  }
  .headline-lead { display: block; font-size: 30px; color: var(--headline-blue); }
  .headline-main { display: block; font-size: 34px; color: var(--headline-green); margin-left: 22px; }
  .appointment {
    position: absolute;
    top: 428px;
    right: 30px;
    text-align: right;
    color: var(--ink-white);
  }
  .appointment-call { font-size: 18px; font-weight: 300; line-height: 23px; }
  .appointment-phone { font-size: 29px; font-weight: 300; margin-top: 4px; letter-spacing: 0.5px; }
  .appointment-address { font-size: 10px; font-weight: 700; line-height: 14px; margin-top: 4px; }
  .brand {
    position: absolute;
    left: 34px;
    bottom: 58px;
    display: flex;
    align-items: center;
    gap: 10px;
  }
  .brand-dot {
    width: 26px; height: 26px;
    border-radius: 50%;
    background: var(--brand-blue);
    flex: none;
  }
  .brand-name {
    font-size: 17px;
    font-weight: 400;
    color: var(--brand-blue);
    letter-spacing: 0.3px;
  }
</style>
</head>
<body>
  <main class="flyer-panel">
    <svg class="panel-shapes" viewBox="0 0 354 820" width="354" height="820">
      <defs>
        <linearGradient id="photo-tone" x1="0" y1="0" x2="0" y2="1">
          <stop offset="0" stop-color="var(--sky-deep)"/>
          <stop offset="0.5" stop-color="var(--sky-mid)"/>
          <stop offset="1" stop-color="var(--sky-pale)"/>
        </linearGradient>
      </defs>
      <polygon class="photo-area" points="0,0 354,0 354,350 0,520" fill="url(#photo-tone)"
        role="img" aria-label="Photo: a happy family of three jumping in the air over a green meadow under a blue sky"/>
      <polygon class="green-band" points="0,520 354,350 354,560 0,720" fill="var(--band-green)"/>
    </svg>

    <h1 class="headline">
      <span class="headline-lead">We Create</span>
      <span class="headline-main">Healthy People</span>
    </h1>

    <section class="appointment">
      <p class="appointment-call">Call today to<br>make an appointment</p>
      <p class="appointment-phone">555-014-2730</p>
      <p class="appointment-address">48 Meadowbrook Ln. suite 210<br>Fairview, VA 20199</p>
    </section>

    <footer class="brand">
      <span class="brand-dot"></span>
      <span class="brand-name">Lakemont Harmony Medical</span>
    </footer>
  </main>
</body>
</html>
```